QRVB registered provider offering Supports for clients

We need a flyer/brochure that we can physically hand out and also one we can send out to our customers.

Small enough for people to hold in their hands, maybe A4/A5 size.

We are a small start-up company that needs to get our services known and out there.

This is our website - https://hollowbrookaid.com.au/

Thank you

```html
<!DOCTYPE html>
<html lang="en">
<head>
<meta charset="utf-8">
<title>Hollowbrook Aid – Flyer</title>
<link rel="stylesheet" href="https://fonts.googleapis.com/css2?family=Montserrat:wght@600;700&family=Open+Sans:wght@400;600&display=swap">
<style>
  :root {
    --purple: #5a2679;
    --green: #83c649;
    --white: #ffffff;
    --ink: #222222;
    --backdrop: #c9c9c9;
    --sage: #c3d6cc;
  }
  * { margin: 0; padding: 0; box-sizing: border-box; }
  html, body { width: 703px; height: 1200px; overflow: hidden; background: var(--backdrop); }
  .flyer {
    position: absolute; left: 0; top: 103px;
    width: 703px; height: 994px;
    background: var(--white); overflow: hidden;
    font-family: "Open Sans", Arial, sans-serif; color: var(--ink);
  }
  .shapes { position: absolute; inset: 0; }
  .brand {
    position: absolute; left: 30px; top: 30px; width: 236px; text-align: center;
  }
  .brand-dot { display: block; width: 34px; height: 34px; border-radius: 50%; background: var(--green); margin: 0 auto 12px; }
  .brand-name { font-family: "Montserrat", Arial, sans-serif; font-weight: 700; font-size: 27px; color: var(--purple); white-space: nowrap; }
  .intro { position: absolute; left: 22px; top: 238px; width: 246px; }
  .intro-title { font-family: "Montserrat", Arial, sans-serif; font-weight: 700; font-size: 25px; color: var(--purple); white-space: nowrap; }
  .intro-rule { width: 74px; height: 4px; background: var(--green); margin: 6px 0 8px; }
  .intro-text { font-size: 12px; line-height: 14.2px; text-align: justify; }
  .provider-note {
    position: absolute; left: 420px; top: 501px;
    font-family: "Montserrat", Arial, sans-serif; font-weight: 700; font-size: 9.5px; line-height: 12px; color: var(--purple);
  }
  .about { position: absolute; left: 22px; top: 532px; width: 313px; color: var(--white); }
  .about-title { font-family: "Montserrat", Arial, sans-serif; font-weight: 700; font-size: 15px; margin-bottom: 8px; }
  .about p { font-size: 10.3px; line-height: 12.7px; text-align: justify; margin-bottom: 12.7px; }
  .services { position: absolute; left: 370px; top: 544px; width: 314px; }
  .services-title { font-family: "Montserrat", Arial, sans-serif; font-weight: 700; font-size: 16px; color: var(--purple); margin-bottom: 5px; }
  .services-text { font-size: 10.3px; line-height: 12.7px; }
  .service-label {
    position: absolute; width: 120px; transform: translateX(-50%); text-align: center;
    font-family: "Montserrat", Arial, sans-serif; font-weight: 700; font-size: 10px; line-height: 12.5px; color: #333;
  }
  .contact-bar {
    position: absolute; left: 0; top: 932px; width: 703px; height: 62px; background: var(--green);
    display: flex; align-items: center; justify-content: space-between; padding: 0 22px;
  }
  .contact-item { display: flex; align-items: center; gap: 6px; font-family: "Montserrat", Arial, sans-serif; font-weight: 600; color: var(--purple); font-size: 11.5px; }
  .contact-item.phone { font-size: 15px; font-weight: 700; }
  .contact-icon { width: 22px; height: 22px; }
</style>
</head>
<body>
<main class="flyer">
  <svg class="shapes" viewBox="0 0 703 994" width="703" height="994">
    <defs>
      <linearGradient id="photoTone" x1="0" y1="0" x2="0.6" y2="1">
        <stop offset="0" stop-color="#c3d6cc"/>
        <stop offset="0.55" stop-color="#d9b8c2"/>
        <stop offset="1" stop-color="#e3bcc9"/>
      </linearGradient>
      <linearGradient id="serviceTone" x1="0" y1="0" x2="1" y2="1">
        <stop offset="0" stop-color="#c9a88e"/>
        <stop offset="1" stop-color="#6c6f86"/>
      </linearGradient>
    </defs>

    <!-- header swoosh -->
    <path d="M0 150 C100 195 220 195 300 160 C220 222 90 232 0 200 Z" fill="var(--purple)"/>
    <path d="M0 200 C90 232 220 222 300 160 C220 236 90 246 0 212 Z" fill="var(--green)"/>

    <!-- hero photograph area -->
    <path d="M345 0 L392 0 C305 100 305 340 405 432 L385 442 C280 345 270 100 345 0 Z" fill="var(--green)"/>
    <path role="img" aria-label="Photo of a smiling child holding out paint-covered hands" d="M392 0 L703 0 L703 465 C600 490 470 480 405 432 C305 340 305 100 392 0 Z" fill="url(#photoTone)"/>
    <path d="M405 432 C470 480 600 490 703 465 L703 492 C600 504 460 492 398 462 Z" fill="var(--purple)"/>

    <!-- about panel -->
    <path d="M0 492 C60 445 120 442 190 472 C240 494 280 486 310 474 L347 474 L347 932 L0 932 Z" fill="var(--purple)"/>
    <path d="M0 478 C60 428 120 428 190 458 C240 480 280 474 310 462 L310 474 C280 486 240 494 190 472 C120 442 60 445 0 492 Z" fill="var(--green)"/>

    <!-- registration badge -->
    <circle cx="342" cy="455" r="80" fill="var(--green)"/>
    <circle cx="342" cy="455" r="72" fill="var(--white)"/>
    <circle cx="342" cy="455" r="66" fill="var(--purple)"/>

    <!-- service thumbnails -->
    <g>
      <circle cx="418" cy="692" r="43" fill="var(--green)"/>
      <circle role="img" aria-label="Photo of two girls giving a thumbs up" cx="424" cy="686" r="42" fill="url(#serviceTone)" stroke="var(--purple)" stroke-width="3"/>
      <circle cx="523" cy="692" r="43" fill="var(--green)"/>
      <circle role="img" aria-label="Photo of a person in a wheelchair at sunset" cx="529" cy="686" r="42" fill="#4a3a3a" stroke="var(--purple)" stroke-width="3"/>
      <circle cx="631" cy="692" r="43" fill="var(--green)"/>
      <circle role="img" aria-label="Photo of a carer helping a client at home" cx="637" cy="686" r="42" fill="#b9a6b4" stroke="var(--purple)" stroke-width="3"/>
      <circle cx="418" cy="840" r="43" fill="var(--green)"/>
      <circle role="img" aria-label="Photo of a modern accessible house" cx="424" cy="834" r="42" fill="#a9b7c2" stroke="var(--purple)" stroke-width="3"/>
      <circle cx="523" cy="840" r="43" fill="var(--green)"/>
      <circle role="img" aria-label="Photo of a boy playing at a day program" cx="529" cy="834" r="42" fill="#6b8fb0" stroke="var(--purple)" stroke-width="3"/>
      <circle cx="631" cy="840" r="43" fill="var(--green)"/>
      <circle role="img" aria-label="Photo of a support coordination meeting" cx="637" cy="834" r="42" fill="#8f9aab" stroke="var(--purple)" stroke-width="3"/>
    </g>
  </svg>

  <header class="brand">
    <span class="brand-dot"></span>
    <div class="brand-name">Hollowbrook Aid</div>
  </header>

  <section class="intro">
    <h1 class="intro-title">Hollowbrook Aid</h1>
    <div class="intro-rule"></div>
    <p class="intro-text">Hollowbrook Aid is a QRVB registered company that specialises in providing comprehensive and personalised support services to individuals with disabilities. As a trusted QRVB service provider, Hollowbrook Aid offers a wide range of supports and assistance to help participants achieve their goals and lead fulfilling lives.</p>
  </section>

  <div class="provider-note">REGISTERED<br>QRVB PROVIDER</div>

  <section class="about">
    <h2 class="about-title">ABOUT US</h2>
    <p>At Hollowbrook Aid, we pride ourselves on our exceptional team of professionals who are dedicated to providing high-quality services as a Quality Regional Validation Body (QRVB) service provider. Our team comprises a diverse group of passionate individuals, each bringing their unique skills and expertise to create a comprehensive support network for our clients.</p>
    <p>Our team includes experienced and qualified support coordinators who are adept at navigating the complexities of the QRVB system. They work closely with our clients, ensuring they have access to the services and resources they need to enhance their quality of life. Our support coordinators are compassionate advocates who go above and beyond to empower individuals with disabilities and their families.</p>
    <p>In addition to support coordinators, we have a team of highly skilled and compassionate allied health professionals. Our occupational therapists, physiotherapists, speech pathologists, and psychologists work collaboratively to address the diverse needs of our clients. They conduct thorough assessments, develop tailored intervention plans, and deliver evidence-based therapies to promote independence, improve communication skills, enhance physical mobility, and support mental well-being.</p>
  </section>

  <section class="services">
    <h2 class="services-title">Our Services</h2>
    <p class="services-text">Hollowbrook Aid’s vision is to empower and enrich the lives of QRVB participants by providing innovative and tailored support services that promote independence, choice, and inclusion in the community.</p>
  </section>

  <div class="service-label" style="left:424px;top:742px">Community<br>Participation</div>
  <div class="service-label" style="left:529px;top:742px">Supported<br>Independent Living</div>
  <div class="service-label" style="left:637px;top:742px">Assistance with<br>Daily Living</div>
  <div class="service-label" style="left:424px;top:890px">Specialist Disability<br>Accommodation</div>
  <div class="service-label" style="left:529px;top:890px">Day<br>Programs</div>
  <div class="service-label" style="left:637px;top:890px">Support<br>Coordination</div>

  <footer class="contact-bar">
    <div class="contact-item phone">
      <svg class="contact-icon" viewBox="0 0 24 24"><circle cx="12" cy="12" r="12" fill="var(--purple)"/><path d="M8.5 6.5l2 2.2-1.2 1.5c.8 1.7 2 2.9 3.6 3.7l1.5-1.2 2.2 2-1.3 1.8c-4.3-.6-7.7-4-8.3-8.3z" fill="var(--white)"/></svg>
      <span>0491570156</span>
    </div>
    <div class="contact-item">
      <svg class="contact-icon" viewBox="0 0 24 24"><circle cx="12" cy="12" r="12" fill="var(--purple)"/><rect x="6.5" y="8" width="11" height="8" rx="1" fill="var(--white)"/><path d="M6.8 8.5l5.2 4 5.2-4" fill="none" stroke="var(--purple)" stroke-width="1.2"/></svg>
      <span>info@hollowbrookaid.com.au</span>
    </div>
    <div class="contact-item">
      <svg class="contact-icon" viewBox="0 0 24 24"><circle cx="12" cy="12" r="12" fill="var(--purple)"/><g fill="none" stroke="var(--white)" stroke-width="1.2"><circle cx="12" cy="12" r="6"/><ellipse cx="12" cy="12" rx="2.6" ry="6"/><path d="M6 12h12M7 9h10M7 15h10"/></g></svg>
      <span>www.hollowbrookaid.com.au</span>
    </div>
  </footer>
</main>
</body>
</html>
```